ROVA Pty Ltd Business Card

Looking for a simple yet eye-catching double-sided business card design using my company logo on one side and contact details on the other.

Target Market(s)

Government

Industry/Entity Type

Communication Systems Engineering

Contact Information for Business Card

ROVA Pty Ltd

Requirements
Nice to have
• Would be great to have a QR code so details can be scanned into contacts

```html
<!DOCTYPE html>
<html lang="en">
<head>
<meta charset="utf-8">
<title>ROVA Pty Ltd – Business Card</title>
<link rel="stylesheet" href="https://fonts.googleapis.com/css2?family=Montserrat:wght@400;500;700;800&display=swap">
<style>
  :root {
    --backdrop: #ecebe8;
    --card: #ffffff;
    --slate: #37424a;
    --ink: #111416;
    --text: #2c343a;
  }
  * { box-sizing: border-box; margin: 0; padding: 0; }
  html, body {
    width: 1200px; height: 960px; overflow: hidden;
    background: var(--backdrop);
    font-family: "Montserrat", sans-serif;
    color: var(--text);
  }
  .sheet {
    width: 1200px; height: 960px;
    display: flex; flex-direction: column; align-items: center; justify-content: center;
    gap: 40px;
  }
  .card {
    position: relative;
    width: 700px; height: 400px;
    background: var(--card);
    border-radius: 40px;
    overflow: hidden;
    box-shadow: 0 6px 18px rgba(0,0,0,0.12);
  }
  .brand {
    display: flex; align-items: center;
    color: var(--slate);
    font-weight: 800;
    letter-spacing: 0.04em;
  }
  .brand-dot {
    border-radius: 50%;
    border: 4px solid var(--slate);
    flex: none;
  }
  /* Front */
  .card-front .brand {
    position: absolute; inset: 0; justify-content: center; gap: 34px;
    font-size: 120px;
  }
  .card-front .brand-dot { width: 110px; height: 110px; }
  /* Back */
  .card-back .brand {
    position: absolute; left: 40px; top: 150px; gap: 18px;
    font-size: 60px;
  }
  .card-back .brand-dot { width: 58px; height: 58px; border-width: 3px; }
  .divider {
    position: absolute; left: 388px; top: 58px;
    width: 2px; height: 220px; background: var(--slate);
  }
  .details {
    position: absolute; left: 414px; top: 56px; width: 270px;
  }
  .person-name {
    font-weight: 800; font-size: 25px; color: var(--slate); letter-spacing: 0.01em;
  }
  .person-role { font-size: 16px; margin-top: 2px; }
  .contact-list { list-style: none; margin-top: 20px; }
  .contact-list li {
    display: flex; align-items: center; gap: 9px;
    font-size: 15.5px; line-height: 26px;
  }
  .contact-list svg { width: 14px; height: 14px; fill: var(--slate); flex: none; }
  .address { margin-top: 16px; font-size: 15.5px; line-height: 22px; }
  .wave { position: absolute; inset: 0; width: 700px; height: 400px; }
</style>
</head>
<body>
<main class="sheet">
  <section class="card card-front" aria-label="Card front">
    <div class="brand"><span class="brand-dot"></span>ROVA</div>
  </section>

  <section class="card card-back" aria-label="Card back">
    <svg class="wave" viewBox="0 0 700 400" aria-hidden="true">
      <path d="M0,400 L0,394 C250,392 430,348 520,326 C610,304 660,300 700,298 L700,400 Z" fill="var(--slate)"/>
      <path d="M0,382 C250,380 430,334 520,312 C610,290 660,286 700,284" fill="none" stroke="var(--ink)" stroke-width="6"/>
    </svg>
    <div class="brand"><span class="brand-dot"></span>ROVA</div>
    <div class="divider"></div>
    <div class="details">
      <p class="person-name">DANIEL REYES</p>
      <p class="person-role">Managing Director</p>
      <ul class="contact-list">
        <li><svg viewBox="0 0 24 24"><path d="M6.6 10.8a15 15 0 0 0 6.6 6.6l2.2-2.2c.3-.3.7-.4 1-.2 1.1.4 2.3.6 3.6.6.6 0 1 .4 1 1V20c0 .6-.4 1-1 1A17 17 0 0 1 3 4c0-.6.4-1 1-1h3.5c.6 0 1 .4 1 1 0 1.3.2 2.5.6 3.6.1.3 0 .7-.2 1z"/></svg>987 654 321</li>
        <li><svg viewBox="0 0 24 24"><path d="M2 5h20v14H2z M2 5l10 8 10-8" fill="var(--slate)"/><path d="M2 6l10 7 10-7" fill="none" stroke="#fff" stroke-width="1.6"/></svg>admin@rova.com.au</li>
        <li><svg viewBox="0 0 24 24"><circle cx="12" cy="12" r="10"/><path d="M2 12h20M12 2c3 3 3 17 0 20M12 2c-3 3-3 17 0 20" fill="none" stroke="#fff" stroke-width="1.4"/></svg>www.rova.com.au</li>
      </ul>
      <p class="address">14-16 Harbour Lane Redfern<br>NSW 2016 Australia</p>
    </div>
  </section>
</main>
</body>
</html>
```